Reproduce my app screenshot to look more updated and modern

My app is a place for farmers to post jobs a when needing help around the Farm, and local farmhands can apply for the job. The Farmer can then review multiple applicants and select the one best fit for the task at hand. I'm trying to give my screens an updated look while keeping my current color scheme and flow. I would like for you guys to recreate this screen with an updated loo the best you can. The main screen with the QV will stay the same. I put that in there to show our logo and our main colors. They look outdated.

Target Market(s)

Farmers and Farm Emlpoyees inside the US

Industry/Entity Type

Agriculture

Requirements
Must have
• and updated look and same buttom/ functionality
Nice to have
Should not have
• dont change the name of any buttons

```html
<!DOCTYPE html>
<html lang="en">
<head>
<meta charset="utf-8">
<title>FieldCrew – App Screens</title>
<link rel="stylesheet" href="https://fonts.googleapis.com/css2?family=Outfit:wght@400;500;600;700&display=swap">
<style>
  :root{
    --stage:#1d5509;
    --brand:#248a45;
    --lime:#8cc54f;
    --lime-soft:#9bd062;
    --screen-bg:#eeeeee;
    --card:#ffffff;
    --ink:#111111;
    --muted:#6a6a6a;
    --line:#e2e2e2;
    --white:#ffffff;
  }
  *{box-sizing:border-box;margin:0;padding:0}
  html,body{width:1200px;height:700px;overflow:hidden}
  body{background:var(--stage);font-family:"Outfit",sans-serif;position:relative;color:var(--ink)}

  .screen{position:absolute;width:344px;overflow:hidden}

  /* splash */
  .splash{left:49px;top:44px;height:611px}
  .splash__photo{position:absolute;inset:0;
    background:linear-gradient(180deg,#8cc552 0%,#86c04f 38%,#74ad40 52%,#4f9a2c 70%,#3d7d20 85%,#4a4a1e 100%)}
  .app-badge{position:absolute;width:119px;height:119px;border-radius:26px;
    background:linear-gradient(160deg,#4fae52,#1f7a38);border:5px solid var(--lime-soft);
    display:flex;align-items:center;justify-content:center;color:var(--white);
    font-weight:700;font-size:40px;letter-spacing:1px;box-shadow:0 8px 18px rgba(0,0,0,.25)}
  .splash .app-badge{left:112px;top:242px}
  .splash__name{position:absolute;left:0;right:0;top:536px;text-align:center;
    color:var(--white);font-weight:700;font-size:31px}

  .loading{left:428px;top:359px;height:341px}
  .loading__photo{position:absolute;inset:0;
    background:linear-gradient(180deg,#8cc552 0%,#8ac352 60%,#7bb546 100%)}
  .loading .app-badge{left:112px;top:229px}

  /* list screens */
  .list-screen{background:var(--screen-bg)}
  .feed{left:428px;top:0;height:327px}
  .home{left:808px;top:45px;height:611px}

  .app-header{position:absolute;left:0;top:0;width:100%;height:85px;background:var(--brand);color:var(--white)}
  .app-header__title{position:absolute;left:0;right:0;top:12px;text-align:center;font-weight:600;font-size:20px;letter-spacing:1px}
  .app-header__menu{position:absolute;right:22px;top:20px;width:15px}
  .app-header__menu span{display:block;height:1.6px;background:var(--white);margin-bottom:4px;border-radius:1px}
  .profile{position:absolute;left:29px;top:51px;display:flex;align-items:center;gap:10px}
  .profile__avatar{width:29px;height:29px;border-radius:50%;background:#d9d9d9;border:2px solid #f2f2f2}
  .profile__name{font-size:11px;font-weight:500}
  .profile__phone{font-size:7.5px;color:var(--lime-soft);margin-top:1px}
  .btn-edit{position:absolute;left:243px;top:54px;width:82px;height:21px;border-radius:3px;
    background:var(--lime);color:var(--white);font-size:8px;display:flex;align-items:center;justify-content:center}

  .post-strip{position:absolute;left:0;top:85px;width:100%;height:30px;background:var(--white)}
  .btn-post{position:absolute;left:22px;top:3px;width:105px;height:23px;border-radius:3px;
    background:linear-gradient(90deg,#1f8040 0%,#2c8a43 55%,var(--lime) 100%);color:var(--white);
    font-size:8px;letter-spacing:.3px;display:flex;align-items:center;justify-content:center}

  .tabs{position:absolute;left:0;top:120px;width:100%;height:31px;background:var(--white);display:flex}
  .tab{flex:1;display:flex;align-items:center;justify-content:center;font-size:11px;color:#666}
  .tab--active{background:var(--lime);color:var(--white);flex:0 0 172px}

  .search{position:absolute;left:17px;top:155px;width:226px;height:28px;background:var(--white);
    font-size:9px;color:#b3b3b3;padding-left:14px;display:flex;align-items:center;border-radius:2px}
  .filter{position:absolute;left:257px;top:155px;width:68px;height:28px;background:var(--white);
    font-size:9px;color:#b3b3b3;display:flex;align-items:center;justify-content:center;gap:8px;border-radius:2px}

  /* job card */
  .job-card{position:absolute;left:17px;width:309px;height:123px;background:var(--card);border-radius:5px;
    box-shadow:0 1px 3px rgba(0,0,0,.05)}
  .job-card__title{position:absolute;left:19px;top:12px;font-size:13.5px;font-weight:600;letter-spacing:.5px}
  .job-row{position:absolute;left:0;width:100%;height:14px}
  .job-row .i{position:absolute;width:11px;height:11px;top:1px;stroke:#8a8a8a;fill:none;stroke-width:1.3}
  .job-row .l{left:21px}.job-row .r{left:208px}
  .job-row .t{position:absolute;top:0;line-height:14px;white-space:nowrap}
  .job-row .tl{left:42px;font-size:11.5px;color:var(--muted)}
  .job-row .tr{left:228px;font-size:8.5px;color:var(--lime)}
  .job-row--meta .tl{font-size:8.5px}
  .job-card__heart{position:absolute;left:243px;top:38px;width:12px;height:11px;fill:var(--lime)}
  .job-card__divider{position:absolute;left:19px;right:19px;top:89px;height:1px;background:var(--line)}
  .fab{position:absolute;left:262px;top:83px;width:36px;height:36px;border-radius:50%;background:var(--lime);
    display:flex;align-items:center;justify-content:center;box-shadow:0 3px 8px rgba(0,0,0,.18)}
  .fab svg{width:15px;height:14px;fill:var(--white)}

  .tab-bar{position:absolute;left:0;bottom:0;width:100%;height:37px;background:var(--white);
    display:flex;justify-content:space-around;align-items:center;padding:0 16px}
  .tab-bar svg{width:18px;height:18px;fill:none;stroke:#333;stroke-width:1.5}
  .tab-bar .on{stroke:none;fill:var(--lime)}
</style>
</head>
<body>
<svg width="0" height="0" style="position:absolute">
  <defs>
    <symbol id="i-bag" viewBox="0 0 12 12"><path d="M4 1.5h4L7 3.5H5zM5 3.5C2 5 1.5 10.5 6 10.5S10 5 7 3.5"/><path d="M6 5.5v3"/></symbol>
    <symbol id="i-pin" viewBox="0 0 12 12"><path d="M6 11S2.5 7 2.5 4.5a3.5 3.5 0 017 0C9.5 7 6 11 6 11z"/><circle cx="6" cy="4.5" r="1.2"/></symbol>
    <symbol id="i-clock" viewBox="0 0 12 12"><circle cx="6" cy="6" r="4.7"/><path d="M6 3.5V6h2"/></symbol>
    <symbol id="i-route" viewBox="0 0 12 12"><path d="M3.5 10.5S1.5 8 1.5 6.5a2 2 0 014 0C5.5 8 3.5 10.5 3.5 10.5zM6.5 9.5c3 0 3-3 1-3.5S8 2 10 2"/><circle cx="10" cy="1.8" r=".8"/></symbol>
    <symbol id="i-case" viewBox="0 0 12 12"><rect x="1" y="3.5" width="10" height="7" rx="1"/><path d="M4.5 3.5v-1.5h3v1.5M1 6.5h10"/></symbol>
    <symbol id="i-heart" viewBox="0 0 12 11"><path d="M6 10.5L1.3 6A2.8 2.8 0 016 2.2 2.8 2.8 0 0110.7 6z"/></symbol>
    <symbol id="i-home" viewBox="0 0 18 18"><path d="M9 2L1.5 9H4v7h4v-4.5h2V16h4V9h2.5z"/></symbol>
    <symbol id="i-search" viewBox="0 0 18 18"><circle cx="7.5" cy="7.5" r="5.5"/><path d="M11.5 11.5l5 5"/></symbol>
    <symbol id="i-list" viewBox="0 0 18 18"><path d="M12 16H3V2h11v8M6 6h6M6 9h6M6 12h3M11 14l2 2 4-4"/></symbol>
    <symbol id="i-plant" viewBox="0 0 18 18"><path d="M1 14l4-2h5l-4 2h6l4-3M9 11V5M9 6c0-3 3-4 6-4-1 3-3 4-6 4zM9 8C8 6 6 5 4 6c1 2 3 2 5 2"/></symbol>
    <symbol id="i-cal" viewBox="0 0 18 18"><rect x="2" y="3" width="14" height="13" rx="1"/><path d="M2 7h14M6 1.5v3M12 1.5v3"/><text x="9" y="14.5" font-size="6.5" text-anchor="middle" stroke="none" fill="#333" font-family="Outfit,sans-serif" font-weight="600">15</text></symbol>
    <symbol id="i-filter" viewBox="0 0 14 14"><path d="M1 3h12M1 7h12M1 11h12"/><circle cx="9" cy="3" r="1.3"/><circle cx="4" cy="7" r="1.3"/><circle cx="8" cy="11" r="1.3"/></symbol>
  </defs>
</svg>

<!-- Splash screen -->
<section class="screen splash">
  <div class="splash__photo" role="img" aria-label="Photo of young corn rows in a misty field"></div>
  <div class="app-badge">QV</div>
  <div class="splash__name">FieldCrew</div>
</section>

<!-- Job feed, scrolled -->
<section class="screen list-screen feed">
  <article class="job-card" style="top:-98px">
    <div class="job-row job-row--meta" style="top:100px">
      <svg class="i l"><use href="#i-route"/></svg><span class="t tl">2.92miles</span>
      <svg class="i r"><use href="#i-case"/></svg><span class="t tr">Apr 1 - Dec 15</span>
    </div>
  </article>
  <article class="job-card" style="top:32px">
    <h3 class="job-card__title">Truck Driver</h3>
    <svg class="job-card__heart"><use href="#i-heart"/></svg>
    <div class="job-row" style="top:38px"><svg class="i l"><use href="#i-bag"/></svg><span class="t tl">$ 12 – 20 per hour</span></div>
    <div class="job-row" style="top:64px"><svg class="i l"><use href="#i-pin"/></svg><span class="t tl">Dewitt, Iowa</span><svg class="i r"><use href="#i-clock"/></svg><span class="t tr">3pm - 3pm</span></div>
    <div class="job-card__divider"></div>
    <div class="job-row job-row--meta" style="top:99px"><svg class="i l"><use href="#i-route"/></svg><span class="t tl">2.92miles</span><svg class="i r"><use href="#i-case"/></svg><span class="t tr">Mar 01 - Feb 28</span></div>
  </article>
  <article class="job-card" style="top:161px">
    <h3 class="job-card__title">Farm Hand, Sprayer, Truck, Repair</h3>
    <svg class="job-card__heart"><use href="#i-heart"/></svg>
    <div class="job-row" style="top:38px"><svg class="i l"><use href="#i-bag"/></svg><span class="t tl">$ 16 – 22 per hour</span></div>
    <div class="job-row" style="top:64px"><svg class="i l"><use href="#i-pin"/></svg><span class="t tl">Dewitt, Iowa</span><svg class="i r"><use href="#i-clock"/></svg><span class="t tr">1am - 1am</span></div>
    <div class="job-card__divider"></div>
    <div class="job-row job-row--meta" style="top:99px"><svg class="i l"><use href="#i-route"/></svg><span class="t tl">6.09miles</span><svg class="i r"><use href="#i-case"/></svg><span class="t tr">Jan 31 -</span></div>
    <div class="fab"><svg><use href="#i-heart"/></svg></div>
  </article>
  <nav class="tab-bar">
    <svg class="on"><use href="#i-home"/></svg>
    <svg><use href="#i-search"/></svg>
    <svg><use href="#i-list"/></svg>
    <svg><use href="#i-plant"/></svg>
    <svg><use href="#i-cal"/></svg>
  </nav>
</section>

<!-- Loading screen -->
<section class="screen loading">
  <div class="loading__photo" role="img" aria-label="Soft green misty field background"></div>
  <div class="app-badge">QV</div>
</section>

<!-- Home screen -->
<section class="screen list-screen home">
  <header class="app-header">
    <div class="app-header__title">FIELDCREW</div>
    <div class="app-header__menu"><span></span><span></span><span></span></div>
    <div class="profile">
      <div class="profile__avatar" role="img" aria-label="Profile photo placeholder"></div>
      <div><div class="profile__name">Daniel Corwin</div><div class="profile__phone">5550147823</div></div>
    </div>
    <div class="btn-edit">Edit Details</div>
  </header>
  <div class="post-strip"><div class="btn-post">POST NEW JOB</div></div>
  <div class="tabs"><div class="tab tab--active">Current Jobs For You</div><div class="tab">Nearby Farmlands</div></div>
  <div class="search">Search Jobs, Farmhands</div>
  <div class="filter">Filter <svg width="13" height="13" fill="none" stroke="#8cc54f" stroke-width="1.1"><use href="#i-filter"/></svg></div>

  <article class="job-card" style="top:187px">
    <h3 class="job-card__title">Seasonal Farm Labor</h3>
    <svg class="job-card__heart"><use href="#i-heart"/></svg>
    <div class="job-row" style="top:38px"><svg class="i l"><use href="#i-bag"/></svg><span class="t tl">$ 12 – 20 per hour</span></div>
    <div class="job-row" style="top:64px"><svg class="i l"><use href="#i-pin"/></svg><span class="t tl">Dewitt, Iowa</span><svg class="i r"><use href="#i-clock"/></svg><span class="t tr">8am - 8am</span></div>
    <div class="job-card__divider"></div>
    <div class="job-row job-row--meta" style="top:99px"><svg class="i l"><use href="#i-route"/></svg><span class="t tl">2.92miles</span><svg class="i r"><use href="#i-case"/></svg><span class="t tr">Apr 1 - Dec 15</span></div>
  </article>
  <article class="job-card" style="top:316px">
    <h3 class="job-card__title">Truck Driver</h3>
    <svg class="job-card__heart"><use href="#i-heart"/></svg>
    <div class="job-row" style="top:38px"><svg class="i l"><use href="#i-bag"/></svg><span class="t tl">$ 12 – 20 per hour</span></div>
    <div class="job-row" style="top:64px"><svg class="i l"><use href="#i-pin"/></svg><span class="t tl">Dewitt, Iowa</span><svg class="i r"><use href="#i-clock"/></svg><span class="t tr">3pm - 3pm</span></div>
    <div class="job-card__divider"></div>
    <div class="job-row job-row--meta" style="top:99px"><svg class="i l"><use href="#i-route"/></svg><span class="t tl">2.92miles</span><svg class="i r"><use href="#i-case"/></svg><span class="t tr">Mar 01 - Feb 28</span></div>
  </article>
  <article class="job-card" style="top:445px">
    <h3 class="job-card__title">Farm Hand, Sprayer, Truck, Repair</h3>
    <svg class="job-card__heart"><use href="#i-heart"/></svg>
    <div class="job-row" style="top:38px"><svg class="i l"><use href="#i-bag"/></svg><span class="t tl">$ 16 – 22 per hour</span></div>
    <div class="job-row" style="top:64px"><svg class="i l"><use href="#i-pin"/></svg><span class="t tl">Dewitt, Iowa</span><svg class="i r"><use href="#i-clock"/></svg><span class="t tr">1am - 1am</span></div>
    <div class="job-card__divider"></div>
    <div class="job-row job-row--meta" style="top:99px"><svg class="i l"><use href="#i-route"/></svg><span class="t tl">6.09miles</span><svg class="i r"><use href="#i-case"/></svg><span class="t tr">Jan 31 -</span></div>
    <div class="fab"><svg><use href="#i-heart"/></svg></div>
  </article>
  <nav class="tab-bar">
    <svg class="on"><use href="#i-home"/></svg>
    <svg><use href="#i-search"/></svg>
    <svg><use href="#i-list"/></svg>
    <svg><use href="#i-plant"/></svg>
    <svg><use href="#i-cal"/></svg>
  </nav>
</section>
</body>
</html>
```